Norwegian psychologist service needs a fresh and exiting web site*

Norwegian psychologist service: working with therapy, personal development, mastery and personal growth. Focus: children and teenagers with special needs; family dynamics; group processes; individuals with a need for therapy and personal growth. (Our company name: Fjordlys og samhold (means Mastery and Growth).

We already have a logo for the company, which will be used (will be attached in the project).

The webside is to be structured in 4 pages with roll down curtain menus (the numbers are just for guiding the designer - the should not be added):

Page 1: Om Fjordlys og Samhold (about Mastery and Growth): this is where our business is is presented/described shortly: Lorem Ipsum dolor cit...

Page 2: Tjenester (Services): this is where our 5 service areas are presented:
2.1 Utredning (Investigation, diagnosing): Lorem Ipsum dolor cit...
2.2 Rådgivning (consulting): Lorem Ipsum dolor cit...

2.3 Kurs og work shops (courses and work shops): Lorem Ipsum dolor cit...
2.3a Fjordlys og samhold Tema 1 (T1)
2.3b Fjordlys og samhold Tema 2 (T2)
2.3c Fjordlys og samhold Tema 3 (T3)

2.4 Terapi og utvikling (Therapy and development)
2.4a Fjordlys og samhold for individer (FS1)
2.4b Fjordlys og samhold i familier (FS2)
2.4c Fjordlys og samhold i grupper (FS3)
2.4d Fjordlys og samhold i institusjoner (FS4)

Page 3: Aktuelt (Blog): this is our blog where we share knowledge and articles

Page 4: Kontakt (Contact): This is the contact form page. Contact form should constitute:
- Ditt navn (your name)
- E-post (your e-mail)
- Emne (subject)
- Melding (message/description)

Our project should also include suggestion for handheld units (iPhone, iPad).
Updates

We have both been traveling with work for a while, and then unfortunately both of us got sick on return, so we need a few more days to evaluate and choose design. Kind Regards Arvid & Margit

Target Market(s)

Focus on therapy, learning, mastery and growth for children and teenagers with special needs, within the family dynamics, or in a group setting.
OUR MARKETS:
Private market: individuals, families, groups and health industry institutions (with focus on learning, mastery, growth (as well as growing up) and psychiatry for children and teenagers with special difficulties and needs)
Public institutions: Government institutions, state institutions and municipality institutions (e.g. schools, municipality health service, hospitals) that serve the public (families with children and teenagers with special needs, and where learning, mastery, growth (as well as growing up) and potential psychiatry is an issue).

Number of Pages Required

4 page

Font styles to use
Sans Serif

Colors

Designer to choose colors to be used in the design.

Requirements
Must have
• The website must have 4 pages with roll down curtain menus (we have added a PDF with suggested structure, and headings, with sub menus - see attached PDF drawing.
• The web page must also use the added logo file - and make the web page work well with our logo.
• We would like the website to have a modern look and we would like the site to be associated with typical HIGH END TOP QUALITY private health institutions, but with a stronger focus on human beings (hands, faces etc), and not white coats and doctors. We are psychologists in the private market.
• For instance, if photos are being used - we tend to like "warm" almost art-like, "grainy" two-tone (e.g. sepia) photos to illustrate our focus. If designer can find such photos as part of design, it would be interesting to us. We would like a few photos like that integrated in the design.
• We also want a design suggestion for how the web page should look like and behave on handheld units (e.g. iPhone, iPad).
Nice to have
• If designer could find a number of suitable photos that matches the business idea and design requirements (see description above), that could follow website, that would be good.
• It could also be nice to have graphic symbols that denote the different pages/subpages (subjects)....
• HORSES: we sometimes use horses as a "tool" in therapy sessions. The horse is not necessarily used for riding, but for contact, communication and grooming. PHOTOS: we would like the designer to find an opportunity for using a photo reflecting this cooperation between therapist, child, teenager and horse. It is a bit up to the designer to find a way to do this... Since the horse is only a tool, among many other tools, it does not have to be much - but we want to try and see how it will work with a photo that also reflects this part of our business.

```html
<!DOCTYPE html>
<html lang="no">
<head>
<meta charset="utf-8">
<title>Fjordlys og Samhold</title>
<link href="https://fonts.googleapis.com/css2?family=Jost:wght@300;400;500;600&display=swap" rel="stylesheet">
<style>
:root{
  --green:#0b6e3a;
  --green-dark:#07602f;
  --blue:#3c4aa3;
  --navy:#2b3a8f;
  --ink:#1d1d1d;
  --muted:#555;
  --line:#c9c9c9;
  --white:#fff;
  --hero-a:#b98a63;
}
*{box-sizing:border-box;margin:0;padding:0}
html,body{width:1200px;height:3623px;overflow:hidden}
body{position:relative;font-family:"Jost",sans-serif;color:var(--ink);background:var(--white)}
.abs{position:absolute}
.center{left:0;width:1200px;text-align:center}
.section-title{font-weight:400;font-size:36px;line-height:1}
.rule{height:3px;width:67px;left:566px}
.btn-solid{background:var(--green);color:var(--white);border-radius:5px;font-size:12px;display:flex;align-items:center;justify-content:center}
.btn-ghost{border:1.5px solid var(--white);color:var(--white);border-radius:5px;font-size:12px;display:flex;align-items:center;justify-content:center}
.arrow{width:60px;height:60px;border-radius:50%;background:#222;border:2px solid rgba(255,255,255,.5);display:flex;align-items:center;justify-content:center}

/* hero */
.hero-bg{left:0;top:0;width:1200px;height:575px;background:linear-gradient(100deg,#c46a4f 0%,var(--hero-a) 35%,#d9c6ad 70%,#c7a07c 100%)}
.hero-shade{left:0;top:0;width:1200px;height:575px;background:rgba(40,25,15,.28)}
.brand{left:160px;top:56px;width:120px;text-align:center;color:var(--white);font-size:16px;font-weight:400;letter-spacing:.5px;line-height:1.1}
.brand-dot{left:208px;top:14px;width:24px;height:24px;border-radius:50%;background:var(--white)}
.nav a{position:absolute;top:40px;color:var(--white);font-size:13px;text-decoration:none;letter-spacing:-.2px;white-space:nowrap}
.nav .cta{top:32px;left:841px;width:110px;height:33px;background:var(--blue);border-radius:4px;display:flex;align-items:center;justify-content:center}
.hero-title{top:226px;font-weight:400;font-size:43px;line-height:1;color:var(--white);letter-spacing:-.5px}
.hero-text{top:292px;left:290px;width:620px;text-align:center;color:var(--white);font-size:12px;line-height:24px}

/* about */
.about-photo{left:177px;top:636px;width:366px;height:366px;border-radius:50%;border:4px solid var(--green);padding:6px;background:var(--white)}
.about-photo div{width:100%;height:100%;border-radius:50%;background:linear-gradient(160deg,#e7e4df,#cfc6bb 60%,#a99888)}
.about-title{left:590px;top:650px;font-weight:400;font-size:34px;line-height:1}
.about-text{left:590px;top:723px;width:440px;font-size:11.5px;line-height:26.6px;color:var(--muted)}

/* services */
.services{left:0;top:1066px;width:1200px;height:659px;background:linear-gradient(90deg,#3a47a0,#4250ad 50%,#3946a0)}
.svc-photo{width:220px;height:220px;border-radius:50%;overflow:hidden}
.svc-badge{width:90px;height:45px;border-radius:45px 45px 0 0;background:var(--green);display:flex;align-items:flex-end;justify-content:center;padding-bottom:6px}
.svc-title{width:320px;text-align:center;color:var(--white);font-size:25px;font-weight:400;line-height:1}
.svc-text{width:250px;text-align:center;color:rgba(255,255,255,.85);font-size:11px;line-height:23px}

/* testimonials */
.quote-text{left:355px;top:1930px;width:530px;text-align:center;font-size:12px;line-height:24px;color:var(--muted)}
.qmark{font-family:Georgia,serif;font-size:120px;color:var(--navy);line-height:1}
.small-arrow{width:36px;height:36px;border-radius:50%;background:var(--white);box-shadow:0 1px 6px rgba(0,0,0,.18);display:flex;align-items:center;justify-content:center}

/* blog */
.blog{left:0;top:2220px;width:1200px;height:622px;background:var(--green-dark)}
.card{width:290px;height:359px;background:var(--white)}
.card-img{position:absolute;left:10px;top:10px;width:270px;height:176px}
.card h3{position:absolute;left:30px;top:204px;font-weight:400;font-size:22px;line-height:1.2}
.card p{position:absolute;left:30px;top:245px;width:232px;font-size:10px;line-height:18px;color:var(--muted)}
.card a{position:absolute;left:30px;top:315px;font-size:11px;letter-spacing:1.4px;color:var(--green);text-decoration:none;font-weight:500}

/* contact */
.field{left:236px;width:392px;height:55px;border:1px solid var(--line);border-radius:4px;display:flex;align-items:center;padding-left:18px;gap:12px;font-size:12px;color:#999}
.info-icon{width:50px;height:50px;border-radius:50%;background:var(--green);display:flex;align-items:center;justify-content:center}
.info{left:750px;font-size:12px;color:var(--ink)}
.social{width:30px;height:30px;border-radius:50%;background:var(--navy)}

/* footer */
.footer{left:0;top:3527px;width:1200px;height:96px;background:var(--green-dark)}
.footer-logo{left:141px;top:3488px;width:186px;height:186px;border-radius:50%;background:var(--white)}
</style>
</head>
<body>

<!-- Hero -->
<section class="hero-bg abs" role="img" aria-label="Foto av en jente med bamse hos en terapeut som noterer"></section>
<div class="hero-shade abs"></div>
<div class="brand-dot abs"></div>
<div class="brand abs">FJORDLYS<br><span style="font-size:10px;letter-spacing:2px">OG SAMHOLD</span></div>
<nav class="nav">
  <a style="left:422px">Home</a>
  <a style="left:484px">Om Fjordlys og Samhold</a>
  <a style="left:627px">Tjenester ▾</a>
  <a style="left:703px">Aktuelt</a>
  <a style="left:770px">Kontakt</a>
  <a class="cta">Be om avtale</a>
</nav>
<h1 class="hero-title abs center">FJORDLYS OG SAMHOLD</h1>
<p class="hero-text abs">Phasellus mattis sit amet ipsum ut posuere. Fusce in faucibus felis. Fusce lobortis lobortis erat vitae aliquet. Vestibulum sodales ultricies turpis, non dapibus sapien maximus vitae.</p>
<div class="btn-solid abs" style="left:547px;top:363px;width:109px;height:32px">Les mer</div>
<div class="arrow abs" style="left:-30px;top:260px"><svg width="20" height="20" viewBox="0 0 20 20" style="margin-left:26px"><path d="M13 3 6 10l7 7" fill="none" stroke="#fff" stroke-width="2.5"/></svg></div>
<div class="arrow abs" style="left:1160px;top:260px"><svg width="20" height="20" viewBox="0 0 20 20" style="margin-right:26px"><path d="m7 3 7 7-7 7" fill="none" stroke="#fff" stroke-width="2.5"/></svg></div>

<!-- About -->
<section class="about">
  <div class="about-photo abs"><div role="img" aria-label="Foto av en smilende psykolog med notatblokk"></div></div>
  <h2 class="about-title abs">Om Fjordlys og Samhold</h2>
  <div class="abs" style="left:590px;top:700px;width:67px;height:3px;background:var(--ink)"></div>
  <p class="about-text abs">Phasellus sem mi, aliquet mattis pulvinar eu, vestibulum a velit. Phasellus venenatis urna nulla, vitae ultrices tellus facilisis in. Duis at placerat enim. Morbi ultrices dolor quis dolor ultrices accumsan eget ac odio. Nam ornare varius est, a molestie eros vestibulum eget. Nulla vel odio id tortor tincidunt ultricies quis at magna. Donec pellentesque imperdiet sagittis. Etiam ut hendrerit purus. Mauris suscipit dolor non est egestas, id dapibus tortor rutrum. Praesent eu magna eget augue mollis egestas vel non lacus. Donec et sapien ut nibh iaculis consequat non vitae ex. Donec cursus elementum pellentesque. Mauris non molestie risus.</p>
  <div class="btn-solid abs" style="left:590px;top:953px;width:109px;height:35px;box-shadow:0 2px 4px rgba(0,0,0,.3)">Les mer</div>
</section>

<!-- Services -->
<section class="services abs" role="img" aria-label="Blått tonet foto av en kvinne i samtale"></section>
<h2 class="section-title abs center" style="top:1128px;color:var(--white);font-size:34px">Tjenester</h2>
<div class="rule abs" style="top:1179px;background:var(--white)"></div>

<div class="svc-photo abs" style="left:176px;top:1238px" role="img" aria-label="Foto av terapeut i samtale med en mann"><div style="width:100%;height:100%;background:linear-gradient(150deg,#a5563f,#e6ddd2 55%,#8a8480)"></div></div>
<div class="svc-photo abs" style="left:490px;top:1238px" role="img" aria-label="Foto av hender og skriveplate under samtale"><div style="width:100%;height:100%;background:linear-gradient(150deg,#5a5550,#b4a79a 55%,#dcd5cc)"></div></div>
<div class="svc-photo abs" style="left:805px;top:1238px" role="img" aria-label="Foto av mor og datter som leker på gulvet"><div style="width:100%;height:100%;background:linear-gradient(150deg,#b98b6a,#e8d6c3 55%,#8aa5a0)"></div></div>

<div class="svc-badge abs" style="left:241px;top:1413px"><svg width="26" height="30" viewBox="0 0 26 30"><rect x="3" y="5" width="20" height="23" rx="2" fill="none" stroke="#fff" stroke-width="2"/><rect x="8" y="2" width="10" height="6" rx="1" fill="none" stroke="#fff" stroke-width="2"/><path d="M8 14h10M8 19h10M8 24h6" stroke="#fff" stroke-width="2"/></svg></div>
<div class="svc-badge abs" style="left:555px;top:1413px"><svg width="28" height="30" viewBox="0 0 28 30"><circle cx="14" cy="6" r="4" fill="none" stroke="#fff" stroke-width="2"/><path d="M6 20c0-5 3-8 8-8s8 3 8 8M3 22h22v6H3z" fill="none" stroke="#fff" stroke-width="2"/></svg></div>
<div class="svc-badge abs" style="left:870px;top:1413px"><svg width="30" height="26" viewBox="0 0 30 26"><path d="M2 3h11l2 2 2-2h11v20H17l-2 2-2-2H2z M15 5v18" fill="none" stroke="#fff" stroke-width="2"/></svg></div>

<div class="svc-title abs" style="left:126px;top:1488px">Utredning</div>
<div class="svc-title abs" style="left:440px;top:1488px">Rådgivning</div>
<div class="svc-title abs" style="left:755px;top:1488px">Kurs og work shops</div>
<p class="svc-text abs" style="left:161px;top:1532px">Cras porttitor metus vel hendrerit sagittis. Suspendisse ornare, eros eget tincidunt efficitur, augue lorem condimentum magna</p>
<p class="svc-text abs" style="left:475px;top:1532px">Cras porttitor metus vel hendrerit sagittis. Suspendisse ornare, eros eget tincidunt efficitur, augue lorem condimentum magna</p>
<p class="svc-text abs" style="left:790px;top:1532px">Cras porttitor metus vel hendrerit sagittis. Suspendisse ornare, eros eget tincidunt efficitur, augue lorem condimentum magna</p>
<div class="btn-ghost abs" style="left:248px;top:1626px;width:77px;height:33px">Les mer</div>
<div class="btn-ghost abs" style="left:561px;top:1626px;width:77px;height:33px">Les mer</div>
<div class="btn-ghost abs" style="left:873px;top:1626px;width:77px;height:33px">Les mer</div>
<div class="arrow abs" style="left:-30px;top:1374px"><svg width="20" height="20" viewBox="0 0 20 20" style="margin-left:26px"><path d="M13 3 6 10l7 7" fill="none" stroke="#fff" stroke-width="2.5"/></svg></div>
<div class="arrow abs" style="left:1160px;top:1374px"><svg width="20" height="20" viewBox="0 0 20 20" style="margin-right:26px"><path d="m7 3 7 7-7 7" fill="none" stroke="#fff" stroke-width="2.5"/></svg></div>

<!-- Testimonials -->
<h2 class="section-title abs center" style="top:1782px">Uttalelser</h2>
<p class="abs center" style="top:1832px;font-size:16px;font-weight:300;color:var(--muted)">Omtaler av vår fornøyde kunde</p>
<div class="rule abs" style="top:1866px;background:var(--ink)"></div>
<div class="qmark abs" style="left:296px;top:1880px">“</div>
<div class="qmark abs" style="left:828px;top:1972px">”</div>
<p class="quote-text abs">Suspendisse faucibus pellentesque neque ac bibendum. Nullam viverra justo ultrices, tincidunt enim nec, congue turpis. Pellentesque suscipit nunc sem, ac congue erat semper vel. In sed velit elementum dolor posuere mattis vel dictum augue. Morbi ac metus a tortor elementum eleifend.</p>
<div class="abs" style="left:560px;top:2024px;width:80px;height:80px;border-radius:50%;background:linear-gradient(160deg,#e6e2dc,#c9ab92 60%,#a06b4c)" role="img" aria-label="Portrett av kunden"></div>
<p class="abs center" style="top:2118px;font-size:17px;font-weight:600">Navn her</p>
<p class="abs center" style="top:2146px;font-size:14px;font-weight:300;color:var(--muted)">klient</p>
<div class="small-arrow abs" style="left:190px;top:1942px"><svg width="12" height="12" viewBox="0 0 12 12"><path d="M8 1 3 6l5 5" fill="none" stroke="#2b3a8f" stroke-width="2"/></svg></div>
<div class="small-arrow abs" style="left:974px;top:1942px"><svg width="12" height="12" viewBox="0 0 12 12"><path d="m4 1 5 5-5 5" fill="none" stroke="#2b3a8f" stroke-width="2"/></svg></div>

<!-- Blog -->
<section class="blog abs"></section>
<h2 class="section-title abs center" style="top:2292px;color:var(--white)">Aktuelt</h2>
<p class="abs center" style="top:2338px;font-size:16px;font-weight:300;color:var(--white)">dette er bloggen vår hvor vi deler kunnskap og artikler</p>
<div class="rule abs" style="top:2373px;background:var(--white)"></div>

<article class="card abs" style="left:141px;top:2414px">
  <div class="card-img" role="img" aria-label="Foto av en bekymret kvinne i en sofa" style="background:linear-gradient(150deg,#d8d4cf,#a98e7c 55%,#e9e7e3)"></div>
  <h3>Tittel her</h3>
  <p>Duis placerat viverra nisl, ac tristique augue aliquet at. Praesent malesuada orci et magna luctus, quis mollis orci rhoncus</p>
  <a>READ MORE</a>
</article>
<article class="card abs" style="left:454px;top:2414px">
  <div class="card-img" role="img" aria-label="Foto av terapeut og ungdom i samtale" style="background:linear-gradient(150deg,#c8b9a5,#e9e6e2 45%,#7f93b0)"></div>
  <h3>Tittel her</h3>
  <p>Duis placerat viverra nisl, ac tristique augue aliquet at. Praesent malesuada orci et magna luctus, quis mollis orci rhoncus</p>
  <a>READ MORE</a>
</article>
<article class="card abs" style="left:768px;top:2414px">
  <div class="card-img" role="img" aria-label="Foto av en smilende kvinne i samtale" style="background:linear-gradient(150deg,#e4e1dc,#b7937b 50%,#dfe2e4)"></div>
  <h3>Tittel her</h3>
  <p>Duis placerat viverra nisl, ac tristique augue aliquet at. Praesent malesuada orci et magna luctus, quis mollis orci rhoncus</p>
  <a>READ MORE</a>
</article>

<!-- Contact -->
<h2 class="section-title abs center" style="top:2900px;font-size:32px">Kontakt</h2>
<div class="field abs" style="top:3033px"><svg width="16" height="16" viewBox="0 0 16 16"><circle cx="8" cy="5" r="3.5" fill="none" stroke="#999"/><path d="M1.5 15c0-4 3-6 6.5-6s6.5 2 6.5 6" fill="none" stroke="#999"/></svg>Ditt navn</div>
<div class="field abs" style="top:3100px"><svg width="18" height="14" viewBox="0 0 18 14"><rect x=".5" y=".5" width="17" height="13" fill="none" stroke="#999"/><path d="m1 1 8 7 8-7M1 13l6-5m10 5-6-5" fill="none" stroke="#999"/></svg>E-post</div>
<div class="field abs" style="top:3166px"><svg width="16" height="16" viewBox="0 0 16 16"><path d="m8 1 2.2 4.6 5 .6-3.7 3.4 1 5L8 12.2 3.5 14.6l1-5L.8 6.2l5-.6z" fill="none" stroke="#999"/></svg>Emne</div>
<div class="field abs" style="top:3233px;height:120px;align-items:flex-start;padding-top:18px"><svg width="16" height="16" viewBox="0 0 16 16"><path d="M11 1.5 14.5 5 5 14.5H1.5V11z" fill="none" stroke="#999"/></svg>Melding</div>
<div class="btn-solid abs" style="left:236px;top:3377px;width:133px;height:39px;font-size:15px;font-weight:600">Sende inn</div>

<div class="info-icon abs" style="left:683px;top:3031px"><svg width="22" height="26" viewBox="0 0 22 26"><path d="M11 25S3 15 3 9.5a8 8 0 0 1 16 0C19 15 11 25 11 25z" fill="none" stroke="#fff" stroke-width="1.8"/><circle cx="11" cy="9.5" r="3" fill="none" stroke="#fff" stroke-width="1.8"/></svg></div>
<p class="info abs" style="top:3032px;font-weight:600">Fjordlys Og Samhold</p>
<p class="info abs" style="top:3057px;font-weight:300">123Integer malesuada in dui varius viverra</p>
<div class="info-icon abs" style="left:683px;top:3127px"><svg width="24" height="24" viewBox="0 0 24 24"><path d="M6 2l4 5-2.5 2.5a13 13 0 0 0 7 7L17 14l5 4-2 4C10 22 2 14 2 4z" fill="none" stroke="#fff" stroke-width="1.8"/></svg></div>
<p class="info abs" style="top:3143px;font-weight:600;letter-spacing:.5px">22-40-5170</p>
<div class="info-icon abs" style="left:683px;top:3217px"><svg width="26" height="18" viewBox="0 0 26 18"><rect x="1" y="1" width="24" height="16" fill="none" stroke="#fff" stroke-width="1.8"/><path d="m1 1 12 9 12-9M1 17l9-7m15 7-9-7" fill="none" stroke="#fff" stroke-width="1.5"/></svg></div>
<p class="info abs" style="top:3234px;font-weight:300">post@fjordlys-eksempel.no</p>
<p class="abs" style="left:682px;top:3334px;font-size:20px;font-weight:600">Follow Me</p>
<div class="social abs" style="left:681px;top:3403px"></div>
<div class="social abs" style="left:731px;top:3403px"></div>
<div class="social abs" style="left:777px;top:3403px"></div>

<!-- Footer -->
<footer class="footer abs"></footer>
<div class="footer-logo abs"></div>
<div class="abs" style="left:222px;top:3510px;width:24px;height:24px;border-radius:50%;background:var(--navy)"></div>
<p class="abs" style="left:141px;top:3545px;width:186px;text-align:center;color:var(--navy);font-size:19px;line-height:1">FJORDLYS<br><span style="font-size:11px;letter-spacing:2px">OG SAMHOLD</span></p>
<p class="abs" style="left:700px;top:3567px;width:400px;text-align:center;color:var(--white);font-size:12px">© COPYRIGHT 2020 FJORDLYS OG SAMHOLD</p>

</body>
</html>
```